Tamarack Hearth Partners Business Card

Looking for a new business card layout. We are a real estate firm w/ a logo, old design attached. Must keep the same elements on there, just need a fresh look and possible some foil accents. Looking for a simpler design w/ more modern style.

Target Market(s)

Real Estate clients

Industry/Entity Type

Real Estate Agent

Contact Information for Business Card

see attached

Font styles to use
Sans Serif

Requirements
Must have
• all elements on current biz card
Nice to have
• modern look, simpler than we have!
Should not have
• no serif fonts

```html
<!DOCTYPE html>
<html lang="en">
<head>
<meta charset="utf-8">
<title>Tamarack Hearth Partners – Business Card</title>
<link rel="stylesheet" href="https://fonts.googleapis.com/css2?family=Arimo:wght@400;700&family=Open+Sans:wght@400&family=Montserrat:wght@800&display=swap">
<style>
  :root {
    --backdrop: #d9d9d9;
    --card-white: #ffffff;
    --ink: #111111;
    --band-black: #0b0b0b;
    --back-black: #101010;
    --text-on-dark: #ffffff;
    --photo-light: #e9dcc8;
    --photo-mid: #d8b68a;
    --photo-teal: #35bfbf;
  }
  * { box-sizing: border-box; margin: 0; padding: 0; }
  html, body { width: 1200px; height: 802px; overflow: hidden; }
  body { background: var(--backdrop); position: relative; }

  .card {
    position: absolute;
    top: 274px;
    width: 442px;
    height: 265px;
    box-shadow: 2px 3px 6px rgba(0,0,0,0.35);
    overflow: hidden;
  }
  .card--front { left: 136px; background: var(--card-white); }
  .card--back { left: 624px; background: var(--back-black); }

  .portrait {
    position: absolute; left: 0; top: 0;
    width: 210px; height: 265px;
    background:
      radial-gradient(ellipse 45% 40% at 45% 42%, var(--photo-mid), transparent 75%),
      linear-gradient(to bottom, var(--photo-light) 0%, var(--photo-light) 60%, var(--photo-teal) 78%, var(--photo-teal) 100%);
  }
  .divider {
    position: absolute; left: 210px; top: 0;
    width: 3px; height: 265px; background: var(--ink);
  }

  .agent { position: absolute; left: 231px; top: 23px; color: var(--ink); }
  .agent__name { font: 700 16.5px/1 "Arimo", sans-serif; letter-spacing: 0.1px; }
  .agent__title { font: 400 10.8px/1.2 "Arimo", sans-serif; margin-top: 1px; }

  .contact-list { position: absolute; left: 231px; list-style: none; color: var(--ink); font: 400 10.6px/15.5px "Open Sans", sans-serif; }
  .contact-list--phones { top: 61px; }
  .contact-list--web { top: 177px; }
  .contact-list li { display: flex; align-items: center; gap: 3px; }
  .contact-list svg { width: 10px; height: 10px; flex: none; }

  .brand-band {
    position: absolute; left: 213px; top: 101px;
    width: 229px; height: 63px;
    background: var(--band-black);
    display: flex; align-items: center; justify-content: center;
  }
  .brand-name {
    color: var(--text-on-dark);
    font: 800 17px/1.1 "Montserrat", sans-serif;
    text-transform: uppercase;
    letter-spacing: 0.2px;
    text-align: center;
  }

  .address { position: absolute; left: 231px; top: 219px; color: var(--ink); font: 400 10.6px/16px "Open Sans", sans-serif; font-style: normal; }

  .card--back {
    display: flex; align-items: center; justify-content: center;
  }
  .card--back .brand-name {
    font-size: 23px;
    line-height: 1.12;
    letter-spacing: 0.3px;
  }
</style>
</head>
<body>
  <section class="card card--front" aria-label="Business card front">
    <div class="portrait" role="img" aria-label="Portrait photo of the agent"></div>
    <div class="divider"></div>

    <header class="agent">
      <h1 class="agent__name">MAREN ELLSWORTH</h1>
      <p class="agent__title">Principal Broker</p>
    </header>

    <ul class="contact-list contact-list--phones">
      <li>
        <svg viewBox="0 0 10 10" aria-hidden="true"><path d="M1 3.2C1 2 3 1.5 5 1.5S9 2 9 3.2v.8H7V3H3v1H1z M2.3 4.6h5.4L9 8.5H1z" fill="#111"/><circle cx="5" cy="6.4" r="1" fill="#fff"/></svg>
        541.555.0142
      </li>
      <li>
        <svg viewBox="0 0 10 10" aria-hidden="true"><rect x="2.6" y="0.5" width="4.8" height="9" rx="0.8" fill="none" stroke="#111" stroke-width="1.1"/><circle cx="5" cy="8" r="0.5" fill="#111"/></svg>
        541.555.0187
      </li>
    </ul>

    <div class="brand-band">
      <p class="brand-name">Tamarack Hearth<br>Partners</p>
    </div>

    <ul class="contact-list contact-list--web">
      <li>
        <svg viewBox="0 0 10 10" aria-hidden="true"><rect x="0.5" y="2" width="9" height="6.2" fill="#111"/><path d="M1 2.5 5 5.8 9 2.5" fill="none" stroke="#fff" stroke-width="0.8"/></svg>
        maren@tamarackhearth.com
      </li>
      <li>
        <svg viewBox="0 0 10 10" aria-hidden="true"><circle cx="5" cy="5" r="4.5" fill="#111"/><path d="M3 2.5c1 .5 1.5 1.5 1 2.5s.5 1.5 1.5 2M6 2c.5 1 1.5 1 2 2" fill="none" stroke="#fff" stroke-width="0.8"/></svg>
        TamarackHearth-Homes.com
      </li>
    </ul>

    <address class="address">210 NW Alder Ave<br>Juniper Falls, OR 97799</address>
  </section>

  <section class="card card--back" aria-label="Business card back">
    <p class="brand-name">Tamarack Hearth<br>Partners</p>
  </section>
</body>
</html>
```